Gift Packaging Beauty Products

I am looking for a gift packaging that can be used for luxurious female beauty products in different sized boxes.

The packaging needs to look like gift already, so people don't even have to wrap it in before giving it to others.

Logo: VELORBEA (see attachment)

Style:
High Class
Trendy Femine
Gift Wrap (see attachment)
Subtle Baroque Patterns/Elements

Colors:
Metallic (Rose) Gold
White

Target Market(s)

Luxurious Female Beauty Products

Industry/Entity Type

Beauty

Font styles to use
Serif
Decorative

Requirements
Must have
• Gift Wrap / Present design
Should not have
• Too busy / too much patterns

```html
<!DOCTYPE html>
<html lang="en">
<head>
<meta charset="utf-8">
<title>Velorbea Gift Wrap</title>
<link href="https://fonts.googleapis.com/css2?family=Playfair+Display:wght@400&display=swap" rel="stylesheet">
<style>
  :root {
    --gold-deep: #bf7a36;
    --gold-mid: #d39a5c;
    --gold-light: #e6bd87;
    --gold-pale: #f1dcc0;
    --white: #ffffff;
    --brand-red: #c0182f;
  }
  html, body {
    margin: 0;
    padding: 0;
    overflow: hidden;
    background: var(--white);
  }
  .wrap {
    position: relative;
    width: 1196px;
    height: 1200px;
    overflow: hidden;
    background: var(--white);
  }
  .damask-field {
    position: absolute;
    left: 0; top: 0;
    width: 1196px; height: 776px;
    background: linear-gradient(90deg,
      var(--gold-pale) 0%, #e2b480 17%, var(--gold-pale) 33%,
      #d8a066 50%, var(--gold-pale) 67%, #e2b480 83%, var(--gold-pale) 100%);
  }
  .damask-field::after {
    content: "";
    position: absolute;
    left: 0; right: 0; bottom: 0;
    height: 22px;
    background: linear-gradient(180deg, rgba(255,255,255,0), rgba(255,255,255,0.75));
  }
  .trim-band {
    position: absolute;
    left: 0; top: 775px;
    width: 1196px; height: 40px;
    background: linear-gradient(90deg, var(--gold-mid), var(--gold-light) 30%, var(--gold-mid) 55%, var(--gold-light) 80%, var(--gold-deep));
    box-shadow: 0 -6px 10px rgba(0,0,0,0.08);
  }
  .trim-band .trim-lace {
    position: absolute;
    left: 0; top: 14px;
    width: 100%; height: 10px;
    background: linear-gradient(90deg, rgba(255,255,255,0.55), rgba(255,255,255,0.8), rgba(255,255,255,0.55));
  }
  .stripe-field {
    position: absolute;
    left: 0; top: 815px;
    width: 1196px; height: 385px;
    background:
      repeating-linear-gradient(90deg, transparent 0 9px, var(--white) 9px 17px),
      linear-gradient(90deg, var(--gold-mid), var(--gold-light) 18%, var(--gold-mid) 35%, var(--gold-deep) 50%, var(--gold-mid) 62%, var(--gold-light) 82%, var(--gold-deep));
  }
  .label {
    position: absolute;
    left: 353px; top: 592px;
    width: 490px; height: 410px;
    filter: drop-shadow(0 8px 10px rgba(0,0,0,0.22));
  }
  .label svg { display: block; }
  .brand-mark {
    position: absolute;
    left: 561px; top: 680px;
    width: 74px; height: 74px;
    border-radius: 50%;
    background: radial-gradient(circle at 40% 35%, var(--gold-pale), var(--gold-light) 55%, var(--gold-mid));
  }
  .brand-name {
    position: absolute;
    left: 353px; top: 806px;
    width: 490px;
    margin: 0;
    padding-left: 0.5em;
    box-sizing: border-box;
    text-align: center;
    font-family: "Playfair Display", serif;
    font-weight: 400;
    font-size: 34px;
    letter-spacing: 0.5em;
    color: var(--brand-red);
    line-height: 1;
  }
  .brand-tagline {
    position: absolute;
    left: 353px; top: 851px;
    width: 490px;
    margin: 0;
    padding-left: 0.45em;
    box-sizing: border-box;
    text-align: center;
    font-family: "Playfair Display", serif;
    font-weight: 400;
    font-size: 12px;
    letter-spacing: 0.45em;
    color: var(--brand-red);
    line-height: 1;
  }
</style>
</head>
<body>
<div class="wrap">
  <div class="damask-field" role="img" aria-label="Repeating baroque floral damask pattern in metallic gold on white"></div>
  <div class="trim-band">
    <div class="trim-lace" role="img" aria-label="Fine white baroque scroll border"></div>
  </div>
  <div class="stripe-field"></div>

  <div class="label">
    <svg width="490" height="410" viewBox="0 0 490 410">
      <defs>
        <linearGradient id="labelGold" x1="0" y1="0" x2="1" y2="1">
          <stop offset="0" stop-color="#e6bd87"/>
          <stop offset="0.45" stop-color="#c9843f"/>
          <stop offset="0.7" stop-color="#e8c597"/>
          <stop offset="1" stop-color="#bf7a36"/>
        </linearGradient>
        <path id="labelShape" d="M0,105 L40,105 Q75,105 95,70 Q120,30 170,28 Q200,28 215,15 Q245,0 275,15 Q290,28 320,28 Q370,30 395,70 Q415,105 450,105 L490,105 L490,305 L450,305 Q415,305 395,340 Q370,382 320,384 Q290,384 275,396 Q245,410 215,396 Q200,384 170,384 Q120,382 95,340 Q75,305 40,305 L0,305 Z"/>
      </defs>
      <use href="#labelShape" fill="#ffffff"/>
      <use href="#labelShape" fill="url(#labelGold)" transform="translate(245 205) scale(0.985) translate(-245 -205)"/>
      <use href="#labelShape" fill="#ffffff" transform="translate(245 205) scale(0.955) translate(-245 -205)"/>
      <use href="#labelShape" fill="none" stroke="url(#labelGold)" stroke-width="3" transform="translate(245 205) scale(0.925) translate(-245 -205)"/>
    </svg>
  </div>

  <div class="brand-mark"></div>
  <h1 class="brand-name">VELORBEA</h1>
  <p class="brand-tagline">BEAUTY PRODUCTS</p>
</div>
</body>
</html>
```